Road Construction Company needs business cards

We would like a new business card designed for our business.

We're a road construction company based in Qld, Australia.

Can the business card please have the following information on it.

Name: Brent Malvoy
Position: General Manager
Phone: 0471 592 304
Email: Brent.malvoy@quendix.com.au
Address: 87 Harrowgate Ave, Pindarra, QLD, 4000
Website: www.quendix.com.au

Visually we'd like the card to be professional and simple.

Attached is our logo.

Our website is www.quendix.com.au

Target Market(s)

Men aged 25-60

Contact Information for Business Card

As listed in project description

Font styles to use
Serif

Requirements
Must have
• Large logo on back of card

```html
<!DOCTYPE html>
<html lang="en">
<head>
<meta charset="utf-8">
<title>Quendix Business Card</title>
<link href="https://fonts.googleapis.com/css2?family=Michroma&family=Arimo:wght@400;700&display=swap" rel="stylesheet">
<style>
  :root {
    --navy: #0b4fa8;
    --royal: #0d5cbf;
    --sky: #2f9fd8;
    --paper: #ffffff;
    --backdrop: #e9eaec;
    --ink: #0b4fa8;
  }
  * { margin: 0; padding: 0; box-sizing: border-box; }
  html, body { width: 1200px; height: 1200px; overflow: hidden; }
  body {
    background: var(--backdrop);
    font-family: "Arimo", Arial, sans-serif;
    display: flex;
    flex-direction: column;
    align-items: center;
    justify-content: center;
    gap: 60px;
  }
  .card {
    width: 900px;
    height: 514px;
    position: relative;
    box-shadow: 0 8px 24px rgba(0,0,0,0.12);
  }
  .card-front { background: var(--paper); }
  .card-back { background: var(--royal); display: flex; align-items: center; justify-content: center; }

  .wordmark {
    font-family: "Michroma", "Arial Black", sans-serif;
    color: var(--navy);
    letter-spacing: 2px;
    line-height: 1;
  }
  .card-front .wordmark { position: absolute; left: 64px; top: 128px; font-size: 54px; }
  .card-back .wordmark { font-size: 96px; color: var(--paper); }

  .rule { position: absolute; height: 7px; }
  .rule-dark { background: var(--navy); }
  .rule-light { background: var(--sky); }
  .rule-top-dark { left: 64px; top: 226px; width: 390px; }
  .rule-top-light { left: 476px; top: 226px; width: 360px; }
  .rule-under-title { left: 64px; top: 352px; width: 390px; }

  .person { position: absolute; left: 64px; top: 262px; }
  .person-name {
    font-family: "Michroma", "Arial Black", sans-serif;
    font-size: 30px;
    color: var(--navy);
    text-transform: uppercase;
    line-height: 1.1;
  }
  .person-title {
    font-family: "Michroma", "Arial Black", sans-serif;
    font-size: 14px;
    color: var(--sky);
    text-transform: uppercase;
    letter-spacing: 1px;
    margin-top: 6px;
  }

  .contacts { position: absolute; list-style: none; }
  .contacts-left { left: 64px; top: 394px; }
  .contacts-right { left: 476px; top: 262px; }
  .contacts li {
    display: flex;
    align-items: center;
    gap: 14px;
    font-size: 19px;
    color: var(--ink);
    height: 42px;
  }
  .icon {
    width: 26px; height: 26px;
    border-radius: 6px;
    background: var(--navy);
    display: flex; align-items: center; justify-content: center;
    flex: none;
  }
  .icon svg { width: 16px; height: 16px; }
</style>
</head>
<body>
  <section class="card card-front" aria-label="Card front">
    <div class="wordmark">QUENDIX</div>
    <div class="rule rule-dark rule-top-dark"></div>
    <div class="rule rule-light rule-top-light"></div>
    <div class="person">
      <div class="person-name">Brent Malvoy</div>
      <div class="person-title">General Manager</div>
    </div>
    <div class="rule rule-dark rule-under-title"></div>
    <ul class="contacts contacts-left">
      <li><span class="icon"><svg viewBox="0 0 16 16"><path d="M4 2 L6.5 2 L7.5 5 L6 6.3 C6.8 8 8 9.2 9.7 10 L11 8.5 L14 9.5 L14 12 C14 13 13 14 12 14 C6.5 13.5 2.5 9.5 2 4 C2 3 3 2 4 2 Z" fill="#fff"/></svg></span>0471 592 304</li>
      <li><span class="icon"><svg viewBox="0 0 16 16"><rect x="2" y="4" width="12" height="9" rx="1" fill="none" stroke="#fff" stroke-width="1.6"/><path d="M2.5 4.5 L8 9 L13.5 4.5" fill="none" stroke="#fff" stroke-width="1.6"/></svg></span>Brent.malvoy@quendix.com.au</li>
    </ul>
    <ul class="contacts contacts-right">
      <li><span class="icon"><svg viewBox="0 0 16 16"><circle cx="8" cy="8" r="5.5" fill="none" stroke="#fff" stroke-width="1.5"/><ellipse cx="8" cy="8" rx="2.4" ry="5.5" fill="none" stroke="#fff" stroke-width="1.2"/><line x1="2.5" y1="8" x2="13.5" y2="8" stroke="#fff" stroke-width="1.2"/></svg></span>www.quendix.com.au</li>
      <li><span class="icon"><svg viewBox="0 0 16 16"><path d="M8 15 C8 15 3 9.5 3 6.5 A5 5 0 0 1 13 6.5 C13 9.5 8 15 8 15 Z" fill="#fff"/><circle cx="8" cy="6.5" r="1.8" fill="#0b4fa8"/></svg></span>87 Harrowgate Ave, Pindarra, QLD, 4000</li>
    </ul>
  </section>

  <section class="card card-back" aria-label="Card back">
    <div class="wordmark">QUENDIX</div>
  </section>
</body>
</html>
```